amber orchard fellowship non profit

I need a simple static website for a non-profit organization that includes blog capacity through Wordpress. The non-profit organization provides education and funding for alternative births and post natal care (doulas and mid-wives) for women. I have the domain name already but not the hosting. I've also set up a gmail account to link to the contact me page.
Updates

Also, would love warm colors.  Background can be white but toolbar and other accents could be peachy warm, tan / mauvish earthy colors.

Thanks.

Target Market(s)

The webstie will be for women who are going through the birthing process or have just given birth. Targeted toward women 16 to 50. The site will include various international outreach programs

Industry/Entity Type

Non Profit

Number of Pages Required

5+ pages

Requirements
Must have
• I want a site that I can control content after it has been designed. So I can add and change copy once it's up. It also must have photo and blog capacity (blog through Wordpress). Toolbar should include (with corresponding pages behind it that I will later include more info that I can update myself) Home, About, Resources / Links, Workshops, Members/Board, Donate Here-sponsors, Forum, International Outreach and somewhere on the homepage: Membership sign-up, Contact.
• The copy attached can be used on the home page.  Then where it explains about the founder, can be in the About section.

• Use warm tones - like peaches or mauvish earthy tan colors for the Toolbars.  (Background can be white.) 
• Use logo (attached) in banner on left and tagline: 
• Non-profit organization providing pre- and postnatal care for women.

• Would like the black and white photo with the mom's hands and baby's feet used as a constant photo and/or in the banner.
Nice to have
• Video capacity for me to add information.  This can be on the blog (through wordpress.)
Should not have
• No stiff, rigid lines.

```html
<!DOCTYPE html>
<html lang="en">
<head>
<meta charset="utf-8">
<title>Amber Orchard Fellowship</title>
<link href="https://fonts.googleapis.com/css2?family=Arimo:wght@400;700&family=Questrial&family=Schoolbell&display=swap" rel="stylesheet">
<style>
  :root{
    --canvas:#efe9e2;
    --paper:#ffffff;
    --band-red:#b50b0b;
    --band-red-dark:#8e0505;
    --pink:#fbc6f5;
    --pink-soft:#f8d9f4;
    --logo-blue:#2a3f9e;
    --nav-cream:#f8f3cf;
    --accent-red:#b30d0d;
    --text-dark:#222222;
    --text-grey:#666666;
    --rule:#b0b0b0;
  }
  *{box-sizing:border-box;margin:0;padding:0}
  html,body{width:1200px;height:686px;overflow:hidden;background:var(--canvas)}
  body{position:relative;font-family:'Arimo',sans-serif;color:var(--text-dark)}
  .site{position:absolute;left:313px;top:2px;width:925px;height:1100px;transform:scale(0.62);transform-origin:0 0}

  .top-sheet{position:absolute;left:112px;top:0;width:778px;height:110px;background:var(--paper);box-shadow:0 2px 8px rgba(0,0,0,.25)}
  .tagline-band{position:absolute;left:16px;top:18px;width:746px;height:80px;background:linear-gradient(var(--band-red),var(--band-red-dark))}
  .tagline{position:absolute;left:20px;top:27px;font-family:'Schoolbell',cursive;color:#fff;font-size:19px}
  .band-icons{position:absolute;right:18px;top:12px;display:flex;gap:18px}

  .main-sheet{position:absolute;left:0;top:95px;width:925px;height:1005px;background:var(--paper);box-shadow:0 4px 14px rgba(0,0,0,.3)}
  .header{position:absolute;left:19px;top:18px;width:886px;height:342px;background:var(--pink)}
  .brand{position:absolute;left:76px;top:170px;display:flex;align-items:center;gap:10px;font-family:'Arimo',sans-serif;font-weight:700;font-size:26px;color:var(--logo-blue)}
  .brand-dot{width:22px;height:22px;border-radius:50%;background:var(--logo-blue)}
  .login{position:absolute;left:76px;top:245px}
  .field{width:186px;height:23px;border:1px solid #aaa;background:#fff;font-size:12px;color:#666;padding:4px 6px;margin-bottom:10px}
  .login-btn{position:absolute;left:200px;top:16px;width:86px;height:24px;background:#fff;font-family:'Schoolbell',cursive;font-size:15px;text-align:center;line-height:24px;transform:rotate(-3deg);box-shadow:1px 2px 3px rgba(0,0,0,.2)}
  .forgot{font-size:10px;margin-top:4px}
  .forgot u{color:#333}
  .hero-photo{position:absolute;left:520px;top:0;width:310px;height:365px;background:radial-gradient(ellipse at 50% 45%,#9a9a9a 0%,#3a3a3a 45%,#050505 75%);transform:rotate(-7deg);box-shadow:2px 3px 8px rgba(0,0,0,.4)}

  .nav{position:absolute;left:30px;top:383px}
  .nav a{display:block;width:175px;height:32px;margin-bottom:15px;background:var(--nav-cream);text-decoration:none;color:var(--text-dark);font-size:14px;letter-spacing:1.5px;text-align:center;line-height:32px;box-shadow:2px 2px 4px rgba(0,0,0,.18)}
  .nav a:nth-child(odd){transform:rotate(-1deg)}
  .nav a:nth-child(even){transform:rotate(1deg)}
  .nav-rule{position:absolute;left:235px;top:385px;height:290px;border-left:1px dashed var(--accent-red)}

  .welcome{position:absolute;left:272px;top:393px;width:453px}
  .welcome h1{font-family:'Questrial',sans-serif;font-weight:400;font-size:38px;color:#555;border-bottom:1px solid var(--rule);line-height:42px}
  .welcome .lead{color:var(--accent-red);font-size:14px;line-height:24px;margin-top:16px}
  .welcome .body{font-size:12px;line-height:24px;margin-top:10px}
  .side-photo{position:absolute;left:755px;top:405px;width:135px;height:160px;background:linear-gradient(135deg,#e0a878,#8c5a38 60%,#3a2a20);border:5px solid #fff;transform:rotate(10deg);box-shadow:2px 3px 6px rgba(0,0,0,.3)}

  .cta-rule{position:absolute;left:62px;top:709px;width:805px;border-top:1px dashed #666}
  .cta{position:absolute;top:722px;display:flex;align-items:baseline;gap:8px;font-family:'Questrial',sans-serif}
  .cta strong{font-weight:400;font-size:24px}
  .cta span{font-family:'Arimo',sans-serif;font-size:13px}
  .cta svg{align-self:center}
  .footer-zone{position:absolute;left:19px;top:730px;width:886px;height:257px;background:linear-gradient(rgba(255,255,255,0),var(--pink-soft) 60%)}
  .card{position:absolute;top:773px;width:236px;text-align:center}
  .card-photo{height:128px;border:5px solid #fff;box-shadow:0 1px 4px rgba(0,0,0,.25)}
  .card h2{font-size:16px;font-weight:400;letter-spacing:.5px;margin-top:16px}
  .card p{font-size:11px;line-height:13px;margin-top:4px}
  .card-rule{position:absolute;top:775px;height:195px;border-left:1px dashed var(--accent-red)}
</style>
</head>
<body>
<div class="site">
  <div class="top-sheet">
    <div class="tagline-band">
      <p class="tagline">Non-profit organization providing pre &amp; postnatal care for women</p>
      <div class="band-icons">
        <svg width="16" height="12" viewBox="0 0 16 12"><rect x="1" y="1" width="14" height="10" fill="none" stroke="#fff"/><path d="M1 1l7 6 7-6" fill="none" stroke="#fff"/></svg>
        <svg width="16" height="14" viewBox="0 0 16 14"><path d="M1 7L8 1l7 6M3 6v7h10V6" fill="none" stroke="#fff"/><rect x="7" y="9" width="2" height="4" fill="#fff"/></svg>
      </div>
    </div>
  </div>

  <div class="main-sheet">
    <div class="header">
      <div class="brand"><span class="brand-dot"></span>Amber Orchard Fellowship</div>
      <form class="login">
        <div class="field">Username</div>
        <div class="field">***********</div>
        <div class="login-btn">LOGIN</div>
        <p class="forgot">Forgot username? <u>Click here</u></p>
      </form>
    </div>
    <div class="hero-photo" role="img" aria-label="Black and white photo of a mother's hands forming a heart around a baby's feet"></div>

    <nav class="nav">
      <a href="#">ABOUT</a><a href="#">RESOURCES</a><a href="#">WORKSHOPS</a><a href="#">FORUM</a><a href="#">BOARD</a>
    </nav>
    <div class="nav-rule"></div>

    <section class="welcome">
      <h1>welcome</h1>
      <p class="lead">Help us help our sisters and daughters to take back control over how we bring the next generation to life</p>
      <p class="body">Phasellus ut placerat risus. Fusce a erat massa. Curabitur sapien massa, tempus euismod aliquam vitae, bibendum ac dui. Class aptent taciti sociosqu ad litora torquent per conubia nostra, per inceptos himenaeos. Aliquam erat volutpat. Pellentesque elementum leo in purus eleifend at iaculis quam commodo. Nulla ante lorem, convallis vel auctor ut, fermentum nec ante. Donec viverra consequat lacus, non sodales nibh suscipit vel. Quisque sagittis velit nec mi placerat suscipit. Nam tincidunt pharetra congue.</p>
    </section>
    <div class="side-photo" role="img" aria-label="Photo of an expectant mother"></div>

    <div class="footer-zone"></div>
    <div class="cta-rule"></div>
    <div class="cta" style="left:62px">
      <svg width="28" height="20" viewBox="0 0 28 20"><path d="M0 0l28 10L0 20l6-10z" fill="var(--accent-red)"/></svg>
      <strong>Join here,</strong><span>free membership and newsletter</span>
    </div>
    <div class="cta" style="left:578px">
      <svg width="28" height="20" viewBox="0 0 28 20"><path d="M0 0l28 10L0 20l6-10z" fill="var(--accent-red)"/></svg>
      <strong>Donate here,</strong><span>for a good cause</span>
    </div>

    <div class="card" style="left:47px">
      <div class="card-photo" role="img" aria-label="Photo of a mother and child outdoors under a blue sky" style="background:linear-gradient(#4a8fd6,#a8d0f0 60%,#3f7a2a)"></div>
      <h2>INTERNATIONAL OUTREACH</h2>
      <p>Adopt/create a healthcare facility overseas</p>
    </div>
    <div class="card-rule" style="left:313px"></div>
    <div class="card" style="left:345px">
      <div class="card-photo" role="img" aria-label="Photo of a newborn holding a parent's hand" style="background:linear-gradient(120deg,#7a5a4e,#c99a88 50%,#e8d0c4)"></div>
      <h2>VOLUNTEERS</h2>
      <p>Doulas, baby sitters, insurance, legal experts, musicians' soothing music, meditations, yogis</p>
    </div>
    <div class="card-rule" style="left:609px"></div>
    <div class="card" style="left:640px">
      <div class="card-photo" role="img" aria-label="Photo of a toddler resting against an adult" style="background:linear-gradient(90deg,#e8c9a4,#c8a888 50%,#8a8478)"></div>
      <h2>EVENTS &amp; NEWS</h2>
      <p>Latest updates &amp; information from around the world</p>
    </div>
  </div>
</div>
</body>
</html>
```